Van wrap for plumbing company on a 2015 rdk tolvera.

I am looking to get a van wrap designed. It is for a plumbing company. The van wrap will be on both sides and the back. The logo on all sides. I want it to pop and be attractive. Using the colors of the logo. Must have logo, email, phone number, and website. Id like the colors to be wavy. I like the look of black on top. Dark blue on the bottom with the logo blown up into the background of the blue. With a touch of the lighter blue in there somewhere., Maybe as a stripe in the middle. Id like a view of all sides, driver, passenger, back, nd hood. I want the phone number to be enlarged on all sides.
Target Market(s)
Home owners of all ages and genders
Industry/Entity Type
Plumbing
Requirements
Must have
- Logo. Email. Info@lumacrest.com phone number (555) 418-6093. Website www.lumacrest.com
Nice to have
- I would like it to pop and be catchy to the e

```html
<!DOCTYPE html>
<html lang="en">
<head>
<meta charset="utf-8">
<title>Lumacrest Plumbing – Van Wrap Side Panel</title>
<link rel="stylesheet" href="https://fonts.googleapis.com/css2?family=Montserrat:wght@600;700;800&display=swap">
<style>
  :root {
    --wrap-blue: #1477bd;
    --wave-light: #8fcaf0;
    --wave-pale: #b9def6;
    --wave-mid: #3f9ad8;
    --tag-black: #0d0d0d;
    --ring-grey: #a7a9ac;
    --badge-white: #ffffff;
    --text-white: #ffffff;
    --brand-blue: #1477bd;
    --photo-sky: #8fbfe6;
    --photo-city: #b49a74;
    --canvas: #ffffff;
  }
  html, body {
    margin: 0;
    width: 1200px;
    height: 1000px;
    overflow: hidden;
    background: var(--canvas);
  }
  .wrap-panel {
    position: absolute;
    left: 50px;
    top: 318px;
    width: 1100px;
    height: 364px;
    display: block;
  }
  .contact-text {
    font-family: "Montserrat", sans-serif;
    font-weight: 700;
    fill: var(--text-white);
  }
  .brand-name {
    font-family: "Montserrat", sans-serif;
    font-weight: 800;
    fill: var(--brand-blue);
  }
</style>
</head>
<body>
<svg class="wrap-panel" viewBox="0 0 918 304" xmlns="http://www.w3.org/2000/svg" aria-label="Lumacrest Plumbing van side wrap">
  <defs>
    <clipPath id="panel-clip"><rect width="918" height="304"/></clipPath>
    <linearGradient id="skyline-fill" x1="0" y1="0" x2="0" y2="1">
      <stop offset="0" stop-color="var(--photo-sky)"/>
      <stop offset="0.45" stop-color="#9fc6e6"/>
      <stop offset="0.55" stop-color="var(--photo-city)"/>
      <stop offset="1" stop-color="#7a6a55"/>
    </linearGradient>
  </defs>

  <g clip-path="url(#panel-clip)">
    <!-- base colour -->
    <rect class="wrap-base" width="918" height="304" fill="var(--wrap-blue)"/>

    <!-- wave bands -->
    <g class="wave-bands">
      <path d="M0 172 C160 150 300 190 470 178 C640 166 760 160 918 172 L918 190 C760 180 640 186 470 196 C300 206 160 170 0 190 Z" fill="var(--wave-light)"/>
      <path d="M0 200 C150 188 320 222 500 210 C660 200 790 196 918 204 L918 214 C790 208 660 214 500 222 C320 232 150 200 0 212 Z" fill="var(--wave-mid)"/>
      <path d="M0 222 C170 208 330 246 520 236 C690 226 800 222 918 228 L918 240 C800 236 690 244 520 252 C330 262 170 228 0 236 Z" fill="var(--wave-light)"/>
      <path d="M0 250 C180 240 320 266 480 264 L480 304 L0 304 Z" fill="var(--wave-pale)"/>
      <path d="M660 250 C740 236 840 236 918 240 L918 304 L640 304 C660 290 700 276 720 272 C690 268 660 262 660 250 Z" fill="var(--wave-pale)"/>
      <path d="M0 282 C120 274 200 290 300 292 L300 304 L0 304 Z" fill="var(--wave-light)"/>
    </g>

    <!-- phone tag -->
    <g class="phone-tag">
      <polygon points="166,153 344,153 336,188 158,188" fill="var(--tag-black)"/>
      <circle cx="181" cy="171" r="10" fill="var(--text-white)"/>
      <path d="M176.5 166.5 c1.2-1.2 2.4-0.8 3 0.6 l0.6 1.6 c0.3 0.8-0.2 1.4-0.9 1.9 c0.8 1.6 1.9 2.7 3.5 3.5 c0.5-0.7 1.1-1.2 1.9-0.9 l1.6 0.6 c1.4 0.6 1.8 1.8 0.6 3 c-4.5 2-12.3-5.8-10.3-10.3 Z" fill="var(--tag-black)"/>
      <text class="contact-text" x="197" y="177.5" font-size="17">(555) 418-6093</text>
    </g>

    <!-- email tag -->
    <g class="email-tag">
      <polygon points="182,204 389,204 381,236 175,236" fill="var(--tag-black)"/>
      <text class="contact-text" x="194" y="225" font-size="14">Info@lumacrest.com</text>
    </g>

    <!-- website bar -->
    <g class="web-bar">
      <rect x="172" y="257" width="480" height="47" fill="var(--tag-black)"/>
      <text class="contact-text" x="208" y="287" font-size="18">www.lumacrest.com</text>
    </g>

    <!-- skyline photo circle -->
    <g class="skyline-window">
      <circle cx="737" cy="106" r="99" fill="var(--tag-black)"/>
      <circle cx="737" cy="106" r="93" fill="url(#skyline-fill)" role="img" aria-label="Photo of a downtown city skyline with office towers under a blue sky"/>
    </g>

    <!-- brand badge -->
    <g class="brand-badge">
      <circle cx="511" cy="124" r="129" fill="var(--tag-black)"/>
      <circle cx="511" cy="124" r="124" fill="var(--ring-grey)"/>
      <circle cx="511" cy="124" r="116" fill="var(--badge-white)"/>
      <text class="brand-name" x="511" y="120" font-size="30" text-anchor="middle">LUMACREST</text>
      <text class="brand-name" x="511" y="152" font-size="22" text-anchor="middle">PLUMBING</text>
    </g>
  </g>
</svg>
</body>
</html>
```